Full stationary package for an IT company specialized in personal cloud solutions
Corvanta Integrated Solutions SDN.BHD.
Full stationary package for an IT company specialized in personal cloud solutions - Information Technology
Creative Brief
Simple
Farid Al Mansoor
Managing Director
Jalan Taman Seroja Indah, No.8 Block F, 17B,2C
farid.mansoor@corvanta-example.com
www.corvanta-example.com
2864019 K
FULL STATIONARY PACKAGE DESIGN PLEASE
Only the LOGO

```html
<!DOCTYPE html>
<html lang="en">
<head>
<meta charset="utf-8">
<title>Corvanta Business Card</title>
<link rel="stylesheet" href="https://fonts.googleapis.com/css2?family=Open+Sans:wght@400;600;700&display=swap">
<style>
  :root {
    --backdrop: #3a3a3a;
    --navy-deep: #163763;
    --navy-mid: #1f4f8c;
    --navy-light: #3a78b8;
    --card-white: #f7f7f7;
    --text-light: #ffffff;
    --text-soft: #d5e2f2;
    --brand-red: #d9342b;
    --brand-orange: #f07a1e;
  }
  html, body {
    margin: 0;
    padding: 0;
    width: 1200px;
    height: 751px;
    overflow: hidden;
    background: var(--backdrop);
    font-family: "Open Sans", Arial, sans-serif;
  }
  .stage {
    position: relative;
    width: 1200px;
    height: 751px;
  }
  .card {
    position: absolute;
    top: 218px;
    width: 497px;
    height: 281px;
    box-sizing: border-box;
  }
  .card-front {
    left: 91px;
    background: linear-gradient(100deg, var(--navy-deep) 0%, var(--navy-mid) 55%, var(--navy-light) 100%);
    color: var(--text-light);
    padding: 30px 36px;
  }
  .card-back {
    left: 593px;
    background: var(--card-white);
  }
  .front-brand {
    margin: 0;
    font-size: 24px;
    font-weight: 700;
    letter-spacing: 1px;
    line-height: 1;
  }
  .holder-name {
    margin: 26px 0 0;
    font-size: 17px;
    font-weight: 600;
    line-height: 1.2;
  }
  .holder-title {
    margin: 2px 0 0;
    font-size: 12px;
    color: var(--text-soft);
  }
  .company-details {
    margin: 18px 0 0;
    font-size: 10.5px;
    line-height: 1.5;
    color: var(--text-soft);
  }
  .contact-list {
    list-style: none;
    margin: 14px 0 0;
    padding: 0;
    font-size: 10.5px;
    line-height: 1.6;
    color: var(--text-soft);
  }
  .contact-list li {
    display: flex;
    align-items: center;
    gap: 8px;
  }
  .contact-icon {
    width: 11px;
    height: 11px;
    flex: none;
  }
  .back-brand {
    position: absolute;
    left: 0;
    right: 0;
    top: 118px;
    display: flex;
    align-items: center;
    justify-content: center;
    gap: 12px;
    padding-left: 60px;
  }
  .back-brand-dot {
    width: 26px;
    height: 26px;
    border-radius: 50%;
    background: var(--brand-orange);
  }
  .back-brand-name {
    font-size: 34px;
    font-weight: 700;
    color: var(--brand-red);
    letter-spacing: 1px;
  }
</style>
</head>
<body>
<main class="stage">
  <section class="card card-front" aria-label="Business card front">
    <p class="front-brand">Corvanta</p>
    <h1 class="holder-name">Farid Al Mansoor</h1>
    <p class="holder-title">Managing Director</p>
    <p class="company-details">
      Lic No. 2864019 K<br>
      Jalan Taman Seroja Indah<br>
      No.8, Block F, 17B,2C
    </p>
    <ul class="contact-list">
      <li>
        <svg class="contact-icon" viewBox="0 0 12 12" aria-hidden="true"><rect x="1" y="4" width="10" height="6" rx="1.5" fill="#ffffff"/><rect x="3" y="2" width="6" height="2.5" rx="1" fill="#ffffff"/></svg>
        +60-01128475902
      </li>
      <li>
        <svg class="contact-icon" viewBox="0 0 12 12" aria-hidden="true"><rect x="1" y="2.5" width="10" height="7" rx="1" fill="#ffffff"/><path d="M1.5 3 L6 6.5 L10.5 3" stroke="#1f4f8c" stroke-width="1" fill="none"/></svg>
        farid.mansoor@corvanta-example.com
      </li>
      <li>
        <svg class="contact-icon" viewBox="0 0 12 12" aria-hidden="true"><circle cx="6" cy="6" r="5" fill="none" stroke="#ffffff" stroke-width="1.2"/><path d="M1 6 H11 M6 1 C3.5 4 3.5 8 6 11 M6 1 C8.5 4 8.5 8 6 11" stroke="#ffffff" stroke-width="0.9" fill="none"/></svg>
        www.corvanta-example.com
      </li>
    </ul>
  </section>

  <section class="card card-back" aria-label="Business card back">
    <div class="back-brand">
      <span class="back-brand-dot"></span>
      <span class="back-brand-name">Corvanta</span>
    </div>
  </section>
</main>
</body>
</html>
```